Wordpress Template Design using existing Logo and Colors

We are wanting a wordpress theme designing for our b2b marketing consultancy business. A comprehesive and elagant design to our current site www.pelvarogroup.com would be good.

Industry/Entity Type

Marketing

Font styles to use
Sans Serif

```html
<!DOCTYPE html>
<html lang="en">
<head>
<meta charset="utf-8">
<title>Pelvaro – B2B Data &amp; Marketing</title>
<link rel="stylesheet" href="https://fonts.googleapis.com/css2?family=Roboto+Condensed:wght@300;400;700&display=swap">
<style>
:root{
  --red:#f2625a;
  --red-dark:#e84c45;
  --red-light:#f8877f;
  --blush:#fdeceb;
  --ink:#555;
  --grey:#888;
  --white:#fff;
  --line:#f4c9c6;
}
*{box-sizing:border-box;margin:0;padding:0}
html,body{width:1200px;height:2852px;overflow:hidden}
body{font-family:"Roboto Condensed",Arial,sans-serif;background:var(--white);color:var(--ink);position:relative}
.page{position:relative;width:1200px;height:2852px;background:var(--white)}

/* nav */
.topbar{position:absolute;left:100px;top:60px;width:1000px;height:40px;background:var(--red);display:flex;align-items:center;justify-content:space-between;padding:0 16px;z-index:2}
.topbar nav{display:flex;gap:28px}
.topbar a{color:var(--white);font-size:13px;font-weight:700;letter-spacing:.5px;text-decoration:none;text-transform:uppercase}
.logo-tab{position:absolute;left:450px;top:60px;width:300px;height:96px;background:var(--white);clip-path:polygon(0 0,100% 0,100% 72%,50% 100%,0 72%);display:flex;align-items:center;justify-content:center;gap:10px;padding-bottom:22px;z-index:5}
.brand{font-weight:700;font-size:38px;line-height:1;color:var(--red);letter-spacing:1px}
.brand-dot{width:12px;height:12px;border-radius:50%;background:var(--red)}

/* hero */
.hero{position:absolute;left:100px;top:100px;width:1000px;height:360px;background:linear-gradient(90deg,var(--red) 0%,var(--red-light) 100%);overflow:hidden;z-index:1}
.hero-visual{position:absolute;right:0;top:0;width:480px;height:360px;background:linear-gradient(90deg,rgba(248,135,127,0) 0%,rgba(255,225,220,.55) 60%,rgba(255,240,238,.7) 100%)}
.hero-copy{position:absolute;left:84px;top:130px;width:400px;color:var(--white)}
.hero-copy h1{font-size:22px;font-weight:700;line-height:1.35;text-transform:uppercase;letter-spacing:.3px}
.hero-copy h1 u{text-underline-offset:3px}
.hero-copy p{font-size:12px;line-height:1.5;margin:12px 0 20px;opacity:.95}
.btn{display:inline-block;padding:9px 16px;font-size:11px;font-weight:700;text-transform:uppercase;letter-spacing:.5px;text-decoration:none}
.btn-light{background:var(--white);color:var(--red)}
.btn-ghost{color:var(--white);border:1px solid transparent;margin-left:8px}
.btn-red{background:var(--red);color:var(--white)}
.btn-outline{border:1px solid var(--white);color:var(--white)}
.arrow{position:absolute;top:162px;width:34px;height:34px;border-radius:50%;background:var(--white);display:flex;align-items:center;justify-content:center}
.arrow.left{left:14px}.arrow.right{right:14px}

/* intro */
.intro{position:absolute;left:120px;top:560px;width:960px;height:170px;background:var(--blush);border-radius:0 40px 40px 0;display:flex;align-items:center;justify-content:space-between;padding:0 60px 0 40px;box-shadow:0 8px 18px rgba(242,98,90,.12)}
.intro p{width:680px;color:var(--red);font-size:13px;line-height:1.6}

/* services */
.service{position:absolute;left:100px;width:1000px;height:300px}
.service-text{position:absolute;width:380px}
.service-text h2{color:var(--red);font-size:17px;font-weight:700;text-transform:uppercase;margin-bottom:12px}
.service-text p{font-size:12px;color:var(--grey);line-height:1.55;margin-bottom:16px}
.service-icon{position:absolute}
.divider{position:absolute;left:100px;width:1000px;height:2px;background:linear-gradient(90deg,transparent,var(--line) 15%,var(--line) 85%,transparent)}

/* brochure */
.brochure{position:absolute;left:100px;top:2215px;width:1000px;height:205px;background:linear-gradient(90deg,var(--red),var(--red-light));text-align:center;color:var(--white);padding-top:38px}
.brochure h2{font-size:18px;font-weight:700;text-transform:uppercase;margin-bottom:10px}
.brochure p{font-size:12px;width:420px;margin:0 auto 18px;line-height:1.5}

/* footer */
.footer{position:absolute;left:100px;top:2420px;width:1000px;height:370px;background:var(--white);display:grid;grid-template-columns:1.3fr 1fr 1fr 1fr;padding:90px 40px 0}
.footer .col{padding:0 24px;border-left:1px solid var(--line);font-size:11px;color:var(--red);line-height:1.8;text-align:center}
.footer .col:first-child{border-left:0;text-align:left;padding-left:0}
.footer .brand{font-size:24px;display:block;margin-bottom:10px}
.footer h3{font-size:13px;font-weight:700;margin-bottom:10px}
.footer ul{list-style:none}
.contact-item{display:flex;flex-direction:column;align-items:center;margin-bottom:10px}
.copyright{position:absolute;left:100px;top:2808px;width:1000px;text-align:center;font-size:10px;color:var(--red)}
</style>
</head>
<body>
<div class="page">

  <header class="topbar">
    <nav><a href="#">Target Marketing</a><a href="#">Data Management</a></nav>
    <nav><a href="#">About</a><a href="#">Contact Us</a></nav>
  </header>
  <div class="logo-tab"><span class="brand">PELVARO</span><span class="brand-dot"></span></div>

  <section class="hero">
    <div class="hero-visual" role="img" aria-label="Businessman in a suit walking towards a bright city skyline with data overlays"></div>
    <div class="hero-copy">
      <h1>Reach the <u>right people</u>, with the <u>right message</u>, at the <u>right time</u></h1>
      <p>Whether your aim is to acquire new customers, re-engage existing ones or grow their value over time, Pelvaro offers tailored solutions.</p>
      <a class="btn btn-light" href="#">Learn More</a><a class="btn btn-ghost" href="#">Get in Touch</a>
    </div>
    <span class="arrow left"><svg width="12" height="12" viewBox="0 0 12 12"><path d="M8 1 3 6l5 5" fill="none" stroke="#f2625a" stroke-width="2"/></svg></span>
    <span class="arrow right"><svg width="12" height="12" viewBox="0 0 12 12"><path d="M4 1l5 5-5 5" fill="none" stroke="#f2625a" stroke-width="2"/></svg></span>
  </section>

  <section class="intro">
    <p>We are a B2B Data, Analytics and Marketing Consulting Company specialised in maximising the power of precise data to strengthen connections between business owners, customers and products. We focus on solutions engineered to meet decision challenges in the data, direct marketing, and analytics space.</p>
    <svg width="44" height="40" viewBox="0 0 44 40"><rect x="0" y="22" width="7" height="16" fill="#f2625a"/><rect x="12" y="10" width="7" height="28" fill="#f2625a"/><rect x="24" y="16" width="7" height="22" fill="#f2625a"/><rect x="36" y="4" width="7" height="34" fill="#f2625a"/></svg>
  </section>

  <section class="service" style="top:860px">
    <svg class="service-icon" style="left:0;top:70px" width="80" height="100" viewBox="0 0 80 100">
      <ellipse cx="40" cy="14" rx="38" ry="12" fill="#f2625a"/>
      <path d="M2 22c0 7 17 12 38 12s38-5 38-12v18c0 7-17 12-38 12S2 47 2 40z" fill="#f2625a"/>
      <path d="M2 48c0 7 17 12 38 12s38-5 38-12v18c0 7-17 12-38 12S2 73 2 66z" fill="#f2625a"/>
      <path d="M2 74c0 7 17 12 38 12s38-5 38-12v12c0 7-17 12-38 12S2 93 2 86z" fill="#f2625a"/>
    </svg>
    <div class="service-text" style="left:460px;top:72px">
      <h2>B2B Database</h2>
      <p>Our access to over 3 million UK business intelligence records and 7 million consumer files gives your campaigns reliable data.</p>
      <a class="btn btn-red" href="#">Learn More</a>
    </div>
  </section>
  <div class="divider" style="top:1160px"></div>

  <section class="service" style="top:1180px">
    <div class="service-text" style="left:0;top:90px">
      <h2>Target Marketing</h2>
      <p>We analyse and build marketing solutions based on your specific objectives, audience and budget to deliver high returns on investment.</p>
      <a class="btn btn-red" href="#">Learn More</a>
    </div>
    <svg class="service-icon" style="left:700px;top:100px" width="80" height="80" viewBox="0 0 80 80">
      <circle cx="40" cy="40" r="36" fill="none" stroke="#f2625a" stroke-width="7"/>
      <circle cx="40" cy="40" r="22" fill="none" stroke="#f2625a" stroke-width="7"/>
      <circle cx="40" cy="40" r="9" fill="#f2625a"/>
    </svg>
  </section>
  <div class="divider" style="top:1475px"></div>

  <section class="service" style="top:1500px">
    <svg class="service-icon" style="left:0;top:90px" width="90" height="100" viewBox="0 0 90 100">
      <path d="M18 18c6-4 10-2 12 3l6 12c2 4 0 7-3 9l-5 3c3 10 9 19 18 26l5-3c3-2 6-2 9 1l9 10c3 3 2 7-2 10l-6 4c-8 5-22-2-33-15S6 38 10 26z" fill="#f2625a"/>
      <path d="M50 20a22 22 0 0 1 16 18" fill="none" stroke="#f2625a" stroke-width="5" stroke-linecap="round"/>
      <path d="M52 6a36 36 0 0 1 28 32" fill="none" stroke="#f2625a" stroke-width="5" stroke-linecap="round"/>
    </svg>
    <div class="service-text" style="left:460px;top:95px">
      <h2>Call Centre</h2>
      <p>When your business requires consultation, our cost effective contact centre services are here to provide the answers you need.</p>
    </div>
  </section>
  <div class="divider" style="top:1860px"></div>

  <section class="service" style="top:1880px">
    <div class="service-text" style="left:0;top:80px">
      <h2>Data Management</h2>
      <p>We nurture your data and supply an effective strategy for storing the data into a profitable resource.</p>
      <a class="btn btn-red" href="#">Learn More</a>
    </div>
    <svg class="service-icon" style="left:800px;top:90px" width="120" height="90" viewBox="0 0 120 90">
      <rect x="0" y="0" width="120" height="22" rx="3" fill="#f2625a"/><circle cx="106" cy="11" r="3" fill="#fff"/>
      <rect x="0" y="33" width="120" height="22" rx="3" fill="#f2625a"/><circle cx="106" cy="44" r="3" fill="#fff"/>
      <rect x="0" y="66" width="120" height="22" rx="3" fill="#f2625a"/><circle cx="106" cy="77" r="3" fill="#fff"/>
    </svg>
  </section>

  <section class="brochure">
    <h2>Corporate Brochure</h2>
    <p>Learn our leading target marketing and intelligent data management solutions to attract new customers for your entire products and services.</p>
    <a class="btn btn-outline" href="#">Download Now</a>
  </section>

  <footer class="footer">
    <div class="col">
      <span class="brand">PELVARO</span>
      <p>Pelvaro is the premier source of market intelligence focused on delivering business opportunities. With one complete, reliable source of data, we help our clients reach the right audience, grow revenue and track results across every channel they use.</p>
    </div>
    <div class="col">
      <h3>Quick Links</h3>
      <ul><li>B2B Database</li><li>Call Centre</li><li>Data Management</li><li>Target Marketing</li><li>About Us</li><li>Contact Us</li><li>Privacy Policy</li></ul>
    </div>
    <div class="col">
      <h3>Visit Us</h3>
      <div class="contact-item"><svg width="12" height="16" viewBox="0 0 12 16"><path d="M6 0a6 6 0 0 1 6 6c0 4-6 10-6 10S0 10 0 6a6 6 0 0 1 6-6z" fill="#f2625a"/><circle cx="6" cy="6" r="2" fill="#fff"/></svg>14 Harbour Lane, Leeds</div>
      <div class="contact-item"><svg width="12" height="16" viewBox="0 0 12 16"><path d="M6 0a6 6 0 0 1 6 6c0 4-6 10-6 10S0 10 0 6a6 6 0 0 1 6-6z" fill="#f2625a"/><circle cx="6" cy="6" r="2" fill="#fff"/></svg>LS1 4BX, United Kingdom</div>
      <div class="contact-item"><svg width="14" height="14" viewBox="0 0 14 14"><circle cx="7" cy="7" r="6" fill="none" stroke="#f2625a" stroke-width="1.5"/><path d="M7 3v4l3 2" fill="none" stroke="#f2625a" stroke-width="1.5"/></svg>Mon – Fri, 9am – 5pm</div>
    </div>
    <div class="col">
      <h3>Reach Us</h3>
      <div class="contact-item"><svg width="14" height="14" viewBox="0 0 14 14"><path d="M3 1c1-1 2 0 3 1l1 2c0 1 0 1-1 2 1 2 2 3 4 4 1-1 1-1 2-1l2 1c1 1 1 2 0 3-3 2-12-7-11-12z" fill="#f2625a"/></svg>+44 (0)20 7946 0321</div>
      <div class="contact-item"><svg width="16" height="12" viewBox="0 0 16 12"><rect x="0.5" y="0.5" width="15" height="11" fill="none" stroke="#f2625a"/><path d="M1 1l7 6 7-6" fill="none" stroke="#f2625a"/></svg>hello@pelvarogroup.com</div>
      <div class="contact-item"><svg width="14" height="14" viewBox="0 0 14 14"><circle cx="7" cy="7" r="6" fill="none" stroke="#f2625a" stroke-width="1.5"/><path d="M1 7h12M7 1c3 3 3 9 0 12M7 1c-3 3-3 9 0 12" fill="none" stroke="#f2625a"/></svg>www.pelvarogroup.com</div>
    </div>
  </footer>
  <div class="copyright">© Pelvaro Group 2024</div>

</div>
</body>
</html>
```